Stretch on the Green with Mara

I want to advertise my Stretch on the Green classes for Summer. Classes are outside at the lovely local park. Dunmore field. 82 Halcombe St. Westlow.
Classes are for beginners to advance levels.
Classes start Monday, October 17th.
Monday 6pm Beginners
Tuesday 6pm Intermediate
Thursday 6pm Intermediate/Advance
Saturday 9am All fitness levels
My Pilates classes are specially designed to help improve strength and flexibility but as well will also improve posture, reduce stress and develop control and endurance in the entire body.
Booking essential. Limited numbers so I can make sure the correct technique is always being followed.
For more info or to book contact details:
Mara 027385916
mara@corestudiomara.net
www.corestudiomara.net
$15 Per Session

Target Market(s)

Males and Females ages 35plus.

Industry/Entity Type

Fitness

Font styles to use
Sans Serif

Requirements
Must have
• My logo. Contact details. A Park that looks lovely to exercise at.
Nice to have
• Summer looking. Trees - inspiration to be exercising outside

```html
<!DOCTYPE html>
<html lang="en">
<head>
<meta charset="utf-8">
<title>Stretch on the Green with Mara – Classes for Summer</title>
<link href="https://fonts.googleapis.com/css2?family=Poppins:wght@400;500;600;700&family=Prata&family=Yellowtail&display=swap" rel="stylesheet">
<style>
  :root {
    --pink: #f587b6;
    --pink-soft: #f7a3c6;
    --green: #14654a;
    --charcoal: #4a4a4b;
    --ink: #1d1d1d;
    --cream: #f4e9df;
    --paper: #ffffff;
    --stage: #e6e6e6;
    --hero-top: #7a914c;
    --hero-bottom: #9cb766;
    --circle-top: #e4e8ea;
    --circle-bottom: #b3aca2;
  }
  * { box-sizing: border-box; margin: 0; padding: 0; }
  html, body { width: 1200px; height: 2245px; overflow: hidden; }
  body { background: var(--stage); font-family: 'Poppins', sans-serif; color: var(--ink); }

  .flyer {
    position: absolute; left: 50px; top: 410px;
    width: 1100px; height: 1424px;
    background: var(--paper);
    overflow: hidden;
    box-shadow: 0 10px 24px rgba(0,0,0,.25);
  }
  .abs { position: absolute; }

  /* hero */
  .hero-photo {
    left: 0; top: 0; width: 1100px; height: 462px;
    background: linear-gradient(180deg, var(--hero-top) 0%, var(--hero-bottom) 100%);
  }
  .hero-fade {
    left: 0; top: 0; width: 1100px; height: 462px;
    background: linear-gradient(90deg, var(--cream) 0%, rgba(244,233,223,.96) 30%, rgba(244,233,223,.55) 46%, rgba(244,233,223,0) 60%);
  }
  .hero-band { left: 0; top: 462px; width: 1100px; height: 12px; background: var(--pink); }

  .brand-tag { left: 65px; top: 0; width: 212px; height: 214px; }
  .brand-name {
    left: 65px; top: 112px; width: 212px; text-align: center;
    font-family: 'Prata', serif; font-size: 17px; color: var(--pink-soft); letter-spacing: .3px;
  }
  .brand-dot { left: 160px; top: 60px; width: 22px; height: 22px; border-radius: 50%; background: #8a8a8a; }

  .title { left: 65px; top: 240px; font-family: 'Prata', serif; line-height: 1; }
  .title-main { font-size: 62px; color: var(--green); letter-spacing: 1px; }
  .title-sub { font-size: 40px; color: var(--ink); margin-top: 2px; }
  .title-script { font-family: 'Yellowtail', cursive; font-size: 42px; color: var(--green); margin-top: 6px; }
  .title-rule { left: 65px; top: 416px; width: 295px; height: 2px; background: var(--ink); }
  .title-rule::before { content: ""; position: absolute; left: -2px; top: -4px; width: 10px; height: 10px; border-radius: 50%; background: var(--ink); }

  .circle-photo {
    left: 734px; top: 320px; width: 298px; height: 298px; border-radius: 50%;
    border: 13px solid var(--pink);
    background: linear-gradient(180deg, var(--circle-top) 0%, var(--circle-bottom) 100%);
  }

  /* location */
  .venue { left: 65px; top: 532px; }
  .venue-lead { font-size: 27px; color: var(--ink); }
  .venue-address { font-size: 27px; font-weight: 700; color: var(--green); margin-top: 6px; letter-spacing: .2px; }
  .venue-frame { left: 65px; top: 548px; width: 667px; height: 80px; }

  .levels-heading {
    left: 0; top: 650px; width: 1100px; text-align: center;
    font-size: 23px; font-weight: 700; color: var(--ink);
  }
  .levels-heading span { color: var(--green); }
  .levels-line { top: 666px; height: 2px; background: var(--pink); }

  /* class cards */
  .class-card {
    top: 786px; width: 212px; height: 239px; border-radius: 16px;
    background: var(--charcoal); color: #fff; text-align: center;
  }
  .class-photo {
    position: absolute; left: 29px; top: -72px; width: 154px; height: 152px;
    border: 5px solid var(--pink); border-radius: 6px;
  }
  .class-level {
    position: absolute; left: 0; top: 98px; width: 100%; height: 50px;
    display: flex; align-items: center; justify-content: center;
    font-size: 20px; font-weight: 700; line-height: 1.05; text-transform: uppercase;
  }
  .class-rule { position: absolute; left: 9px; right: 9px; top: 148px; height: 2px; background: #b9b9b9; }
  .class-time { position: absolute; left: 0; top: 168px; width: 100%; font-size: 21px; }
  .class-time b { font-weight: 500; border: 2px solid var(--pink); padding: 0 4px; margin-left: 4px; }

  /* start + description */
  .start {
    left: 0; top: 1046px; width: 1100px; text-align: center;
    font-size: 29px; font-weight: 700; color: var(--green);
    display: flex; align-items: center; justify-content: center; gap: 30px;
  }
  .start em { font-style: normal; color: var(--ink); }
  .lotus { width: 34px; height: 22px; }
  .about {
    left: 80px; top: 1096px; width: 940px; text-align: center;
    font-size: 21px; line-height: 1.25; color: var(--ink);
  }

  .booking-box { left: 89px; top: 1205px; width: 696px; height: 78px; border: 2px solid var(--ink); border-top: 0; }
  .booking-box::before { content: ""; position: absolute; left: 269px; right: -2px; top: 0; height: 2px; background: var(--ink); }
  .booking-tag {
    left: 80px; top: 1189px; width: 278px; height: 36px; background: var(--pink);
    border-radius: 14px 0 0 0; font-size: 23px; font-weight: 600; color: var(--ink);
    padding-left: 14px; line-height: 38px;
  }
  .booking-text { left: 108px; top: 1228px; width: 660px; font-size: 21px; line-height: 1.05; color: var(--ink); }

  .price { left: 847px; top: 1160px; width: 160px; height: 160px; }
  .price-value {
    left: 847px; top: 1176px; width: 160px; text-align: center;
    font-size: 62px; font-weight: 700; color: #fff; line-height: 1;
  }
  .price-value sup { font-size: 30px; vertical-align: 22px; margin-right: 2px; }
  .price-rule { left: 872px; top: 1247px; width: 110px; height: 2px; background: #fff; }
  .price-note { left: 847px; top: 1252px; width: 160px; text-align: center; font-size: 17px; color: #fff; }

  /* footer */
  .footer-band { left: 0; top: 1335px; width: 1100px; height: 89px; background: var(--charcoal); }
  .footer-cta { left: 0; top: 1318px; width: 430px; height: 106px; }
  .footer-cta-text { left: 65px; top: 1348px; font-size: 23px; font-weight: 600; line-height: 1.1; color: var(--ink); }
  .contact { color: #fff; font-size: 21px; display: flex; align-items: center; gap: 14px; }
  .contact svg { width: 26px; height: 26px; flex: none; }
  .contact-phone { left: 430px; top: 1364px; }
  .contact-mail { left: 690px; top: 1344px; }
  .contact-web { left: 690px; top: 1378px; }
</style>
</head>
<body>
<main class="flyer">

  <!-- hero -->
  <div class="abs hero-photo" role="img" aria-label="Photo of a sunlit park with trees and a group exercising on mats on the grass"></div>
  <div class="abs hero-fade"></div>
  <div class="abs hero-band"></div>

  <svg class="abs brand-tag" viewBox="0 0 212 214" aria-hidden="true">
    <polygon points="0,0 212,0 212,175 106,214 0,175" fill="var(--charcoal)"/>
  </svg>
  <div class="abs brand-dot"></div>
  <div class="abs brand-name">Stretch with Mara</div>

  <div class="abs title">
    <div class="title-main">STRETCH</div>
    <div class="title-sub">ON THE GREEN</div>
    <div class="title-script">Classes for Summer</div>
  </div>
  <div class="abs title-rule"></div>

  <div class="abs circle-photo" role="img" aria-label="Photo of a woman stretching on a boardwalk by the sea"></div>

  <!-- location -->
  <svg class="abs venue-frame" viewBox="0 0 667 80" aria-hidden="true">
    <polyline points="590,8 662,8 662,78 4,78" fill="none" stroke="var(--ink)" stroke-width="2.5"/>
    <circle cx="5" cy="78" r="5" fill="var(--ink)"/>
  </svg>
  <div class="abs venue">
    <p class="venue-lead">Classes are outside at the lovely local park</p>
    <p class="venue-address">DUNMORE FIELD (82 HALCOMBE ST. WESTLOW)</p>
  </div>

  <div class="abs levels-line" style="left:105px;width:125px"></div>
  <div class="abs levels-line" style="left:870px;width:125px"></div>
  <h2 class="abs levels-heading">CLASSES ARE FOR <span>BEGINNERS TO ADVANCE LEVELS</span></h2>

  <!-- class cards -->
  <article class="abs class-card" style="left:65px">
    <div class="class-photo" role="img" aria-label="Photo of a man in a side-angle stretch in a park" style="background:linear-gradient(180deg,#8fb863 0%,#5e8f3e 100%)"></div>
    <div class="class-level">Beginners</div>
    <div class="class-rule"></div>
    <div class="class-time">Monday<b>6pm</b></div>
  </article>
  <article class="abs class-card" style="left:320px">
    <div class="class-photo" role="img" aria-label="Photo of a woman in a wide lunge on autumn leaves" style="background:linear-gradient(180deg,#9a7a42 0%,#8a4f22 100%)"></div>
    <div class="class-level">Intermediate</div>
    <div class="class-rule"></div>
    <div class="class-time">Tuesday<b>6pm</b></div>
  </article>
  <article class="abs class-card" style="left:573px">
    <div class="class-photo" role="img" aria-label="Photo of a woman in an advanced seated back-bend pose" style="background:linear-gradient(180deg,#f1f2f4 0%,#d6d9de 100%)"></div>
    <div class="class-level">Intermediate<br>/Advance</div>
    <div class="class-rule"></div>
    <div class="class-time">Thursday<b>6pm</b></div>
  </article>
  <article class="abs class-card" style="left:823px">
    <div class="class-photo" role="img" aria-label="Photo of a group class stretching in a bright studio" style="background:linear-gradient(180deg,#ddd0c6 0%,#6e6664 100%)"></div>
    <div class="class-level">All Fitness<br>Levels</div>
    <div class="class-rule"></div>
    <div class="class-time">Saturday<b>9am</b></div>
  </article>

  <!-- start + description -->
  <h3 class="abs start">
    <svg class="lotus" viewBox="0 0 34 22" aria-hidden="true"><g fill="var(--pink)"><ellipse cx="17" cy="10" rx="5" ry="10"/><ellipse cx="9" cy="13" rx="4" ry="8" transform="rotate(-30 9 13)"/><ellipse cx="25" cy="13" rx="4" ry="8" transform="rotate(30 25 13)"/><ellipse cx="17" cy="20" rx="15" ry="2.5"/></g></svg>
    <span>CLASSES START MONDAY, <em>OCTOBER 17TH</em></span>
    <svg class="lotus" viewBox="0 0 34 22" aria-hidden="true"><g fill="var(--pink)"><ellipse cx="17" cy="10" rx="5" ry="10"/><ellipse cx="9" cy="13" rx="4" ry="8" transform="rotate(-30 9 13)"/><ellipse cx="25" cy="13" rx="4" ry="8" transform="rotate(30 25 13)"/><ellipse cx="17" cy="20" rx="15" ry="2.5"/></g></svg>
  </h3>
  <p class="abs about">My Pilates classes are specially designed to help improve strength and flexibility but as well will also improve posture, reduce stress and develop control and endurance in the entire body.</p>

  <div class="abs booking-box"></div>
  <div class="abs booking-tag">BOOKING ESSENTIAL</div>
  <p class="abs booking-text">Limited numbers so I can make sure the correct technique is always being followed.</p>

  <svg class="abs price" viewBox="0 0 160 160" aria-hidden="true">
    <polygon fill="var(--charcoal)" stroke="var(--charcoal)" stroke-width="6" stroke-linejoin="round"
      points="158,80 145.7,97.6 147.5,119 128.1,128.1 119,147.5 97.6,145.7 80,158 62.4,145.7 41,147.5 31.9,128.1 12.5,119 14.3,97.6 2,80 14.3,62.4 12.5,41 31.9,31.9 41,12.5 62.4,14.3 80,2 97.6,14.3 119,12.5 128.1,31.9 147.5,41 145.7,62.4"/>
  </svg>
  <div class="abs price-value"><sup>$</sup>15</div>
  <div class="abs price-rule"></div>
  <div class="abs price-note">Per Session</div>

  <!-- footer -->
  <div class="abs footer-band"></div>
  <svg class="abs footer-cta" viewBox="0 0 430 106" aria-hidden="true">
    <polygon points="0,0 430,0 400,106 0,106" fill="var(--pink)"/>
  </svg>
  <p class="abs footer-cta-text">For more info or to book<br>contact details</p>

  <div class="abs contact contact-phone">
    <svg viewBox="0 0 26 26" aria-hidden="true"><rect x="1" y="1" width="24" height="24" rx="6" fill="#fff"/><path d="M8 6.5c1-.6 1.8-.4 2.3.6l1 2c.3.7.1 1.3-.5 1.7l-.8.5c.6 1.7 1.9 3 3.6 3.7l.5-.8c.4-.6 1-.8 1.7-.5l2 1c1 .5 1.2 1.3.6 2.3-1 1.6-2.6 2-4.3 1.3-3.3-1.4-5.9-4-7.3-7.3C6.5 9.1 6.9 7.5 8 6.5z" fill="var(--charcoal)"/></svg>
    <span>027385916(Mara)</span>
  </div>
  <div class="abs contact contact-mail">
    <svg viewBox="0 0 26 26" aria-hidden="true"><rect x="1" y="1" width="24" height="24" rx="6" fill="#fff"/><rect x="6" y="8" width="14" height="10" fill="none" stroke="var(--charcoal)" stroke-width="1.6"/><polyline points="6,8 13,14 20,8" fill="none" stroke="var(--charcoal)" stroke-width="1.6"/></svg>
    <span>mara@corestudiomara.net</span>
  </div>
  <div class="abs contact contact-web">
    <svg viewBox="0 0 26 26" aria-hidden="true"><rect x="1" y="1" width="24" height="24" rx="6" fill="#fff"/><g fill="none" stroke="var(--charcoal)" stroke-width="1.4"><circle cx="13" cy="13" r="7"/><ellipse cx="13" cy="13" rx="3" ry="7"/><line x1="6" y1="13" x2="20" y2="13"/></g></svg>
    <span>www.corestudiomara.net</span>
  </div>

</main>
</body>
</html>
```